Chartered Professional Accounting Firm Needs a Business Card Design

We need a card design for an accounting firm based in Toronto, Ontario. The firm name is Lorne Patek Professional Corporation. The owner of the firm is a chartered professional accountant and a certified general accountant. Services of the firm include 60% tax preparation and consulting and 40% financial statements for corporation year-end. We would like a modern design. The color could be black, white, gray, blue or other color to bring more confidence to clients. The logo of the firm should be included in the design. Thanks
Updates

Name: Lorne Patek, CPA, CGA Address: 47 Marrow Creek Rd. Richmond Hill, ON K7T 5P3 Telephone: (416) 555-0142 Fax:(416) 555-0187 Email: lorne@lornepatek.example

Industry/Entity Type

Accounting

```html
<!DOCTYPE html>
<html lang="en">
<head>
<meta charset="utf-8">
<title>Lorne Patek Professional Corporation – Business Card</title>
<link rel="stylesheet" href="https://fonts.googleapis.com/css2?family=Open+Sans:wght@400;600;700&display=swap">
<style>
  :root {
    --backdrop: #2b2b2b;
    --card-white: #ffffff;
    --brand-blue: #3c3ca0;
    --brand-gray: #8a8a8f;
  }
  html, body {
    margin: 0;
    padding: 0;
    width: 1200px;
    height: 1000px;
    overflow: hidden;
    background: var(--backdrop);
    font-family: "Open Sans", Arial, sans-serif;
  }
  .card {
    position: absolute;
    left: 150px;
    top: 243px;
    width: 900px;
    height: 514px;
    background: var(--card-white);
    overflow: hidden;
  }
  .card-shapes {
    position: absolute;
    inset: 0;
  }
  .brand-mark {
    position: absolute;
    left: 70px;
    top: 70px;
    display: flex;
    align-items: center;
    gap: 16px;
    color: var(--brand-blue);
    font-weight: 700;
    font-size: 30px;
    letter-spacing: 1px;
    text-transform: uppercase;
  }
  .brand-square {
    width: 90px;
    height: 90px;
    background: var(--brand-blue);
  }
  .contact {
    position: absolute;
    right: 70px;
    top: 50px;
    color: var(--brand-blue);
    font-size: 19px;
    line-height: 1.4;
  }
  .contact-row {
    display: grid;
    grid-template-columns: auto auto;
    column-gap: 8px;
    justify-content: end;
  }
  .contact-label {
    font-weight: 700;
    text-align: right;
  }
  .contact-gap { height: 26px; }
  .holder-name {
    position: absolute;
    left: 205px;
    top: 412px;
    color: var(--card-white);
    font-size: 26px;
    white-space: nowrap;
  }
  .holder-credentials {
    font-size: 15px;
  }
  .firm-lockup {
    position: absolute;
    left: 600px;
    top: 362px;
    display: flex;
    align-items: center;
    gap: 10px;
    color: var(--brand-blue);
    font-weight: 600;
  }
  .firm-square {
    width: 46px;
    height: 46px;
    background: var(--brand-blue);
    flex: none;
  }
  .firm-text { line-height: 1.2; white-space: nowrap; }
  .firm-name { font-size: 22px; letter-spacing: 1px; text-transform: uppercase; }
  .firm-sub { font-size: 9px; text-transform: uppercase; letter-spacing: 0.3px; }
</style>
</head>
<body>
  <section class="card" aria-label="Business card for Lorne Patek Professional Corporation">
    <svg class="card-shapes" width="900" height="514" viewBox="0 0 900 514" aria-hidden="true">
      <path d="M0 345 L900 285 L900 514 L0 514 Z" fill="var(--brand-blue)"/>
      <circle cx="760" cy="520" r="240" fill="var(--card-white)"/>
    </svg>

    <div class="brand-mark">
      <span class="brand-square"></span>
      <span>Lorne Patek</span>
    </div>

    <div class="contact">
      <div class="contact-row"><span class="contact-label">Address :</span><span>47 Marrow Creek Rd.</span></div>
      <div class="contact-row"><span class="contact-label"></span><span>Richmond Hill,</span></div>
      <div class="contact-row"><span class="contact-label"></span><span>ON K7T 5P3</span></div>
      <div class="contact-gap"></div>
      <div class="contact-row"><span class="contact-label">Tel :</span><span>(416) 555-0142</span></div>
      <div class="contact-row"><span class="contact-label">Fax :</span><span>(416) 555-0187</span></div>
      <div class="contact-row"><span class="contact-label">Email :</span><span>lorne@lornepatek.example</span></div>
    </div>

    <div class="holder-name">Lorne Patek,<span class="holder-credentials">CPA, CGA</span></div>

    <div class="firm-lockup">
      <span class="firm-square"></span>
      <div class="firm-text">
        <div class="firm-name">Lorne Patek</div>
        <div class="firm-sub">Professional Corporation</div>
        <div class="firm-sub">Chartered Professional Accountant</div>
        <div class="firm-sub">Certified General Accountant</div>
      </div>
    </div>
  </section>
</body>
</html>
```